Roofing Company needs Business card design

We need a business card design for our roofing contracting company. We do Residential and commercial roofing. Design need to be modern, professional and clean. The design should communicate quality and professionalism. We would like to have rounded corners, but open to your ideas.
Company Name: Kestrel roofing Solutions
Company Address: (dummy text)
Name on business card: (dummy text)
And following lines:
Storm damage specialists
commercial & residential
shingles, flat and metal roofs./
Open to background colors.
I have ai. and eps files of logo if needed.
just let me know.
Mostly residential customers but we do commercial too.
Roofing

```html
<!DOCTYPE html>
<html lang="en">
<head>
<meta charset="utf-8">
<title>Kestrel roofing Solutions – Business Card</title>
<link rel="stylesheet" href="https://fonts.googleapis.com/css2?family=Open+Sans:wght@400;600;700&display=swap">
<style>
  :root {
    --canvas: #e9e6e1;
    --ink: #1a1a1a;
    --card-black: #141414;
    --card-black-soft: #2a2a2a;
    --paper: #ffffff;
    --orange: #f26a21;
    --orange-deep: #d8332a;
    --muted-white: #f2f2f2;
    --faint: #2f2c2a;
  }
  * { box-sizing: border-box; margin: 0; padding: 0; }
  html, body {
    width: 1200px; height: 1014px; overflow: hidden;
    background: var(--canvas);
    font-family: "Open Sans", Arial, sans-serif;
  }
  .sheet {
    position: relative; width: 1200px; height: 1014px;
  }
  .card {
    position: absolute; left: 280px; width: 640px; height: 366px;
    border-radius: 24px; overflow: hidden;
    box-shadow: 0 10px 28px rgba(0,0,0,0.18);
  }
  .card--front { top: 90px; background: var(--paper); }
  .card--back {
    top: 540px;
    background: linear-gradient(160deg, var(--card-black-soft) 0%, var(--card-black) 55%, #0b0b0b 100%);
  }

  /* front */
  .front-art { position: absolute; inset: 0; }
  .holder { position: absolute; left: 44px; top: 92px; }
  .holder__name { font-size: 25px; font-weight: 700; color: var(--ink); line-height: 1.1; }
  .holder__role { font-size: 19px; font-weight: 600; color: var(--orange); margin-left: 78px; margin-top: 2px; }

  .brand {
    position: absolute; right: 40px; top: 46px;
    display: flex; align-items: center; gap: 12px;
  }
  .brand__dot { width: 22px; height: 22px; border-radius: 50%; background: var(--orange); }
  .brand__name { font-size: 27px; font-weight: 700; color: var(--ink); letter-spacing: 0.3px; }

  .contact {
    position: absolute; left: 70px; top: 232px;
    color: var(--muted-white); font-size: 19px; line-height: 30px;
  }
  .address {
    position: absolute; right: 44px; top: 188px; text-align: right;
    color: var(--muted-white); font-size: 19px; line-height: 30px;
  }

  /* back */
  .services {
    position: absolute; left: 48px; top: 40px; list-style: none;
    color: var(--muted-white); font-size: 21px; font-weight: 600; line-height: 40px;
  }
  .services li { display: flex; align-items: center; gap: 14px; }
  .services li::before {
    content: ""; width: 9px; height: 9px; border-radius: 50%; background: var(--orange);
  }
  .back-wordmark {
    position: absolute; right: -10px; bottom: 10px;
    font-size: 120px; font-weight: 700; color: var(--faint); line-height: 1;
  }
</style>
</head>
<body>
<main class="sheet">
  <section class="card card--front" aria-label="Business card front">
    <svg class="front-art" width="640" height="366" viewBox="0 0 640 366" aria-hidden="true">
      <path d="M0 172 L108 172 L124 150 L196 150 L196 172 L640 172 L640 366 L0 366 Z" fill="var(--card-black)"/>
      <path d="M0 172 L108 172 L124 150 L196 150 L196 172 L640 172" fill="none" stroke="var(--orange)" stroke-width="4"/>
      <rect x="0" y="326" width="640" height="8" fill="var(--paper)"/>
      <rect x="0" y="334" width="640" height="4" fill="var(--orange)"/>
      <rect x="0" y="338" width="640" height="28" fill="var(--paper)"/>
    </svg>
    <div class="holder">
      <p class="holder__name">Daniel Ostrander</p>
      <p class="holder__role">owner</p>
    </div>
    <div class="brand">
      <span class="brand__dot"></span>
      <span class="brand__name">Kestrel roofing Solutions</span>
    </div>
    <div class="address">
      <p>Kestrel roofing Solutions</p>
      <p>412 Cedar Ridge Road</p>
      <p>10482 NY, Millbrook</p>
    </div>
    <div class="contact">
      <p>phone 555.214.0637</p>
      <p>daniel@kestrelroofing.net</p>
      <p>www.kestrelroofing.net</p>
    </div>
  </section>

  <section class="card card--back" aria-label="Business card back">
    <span class="back-wordmark">Kestrel</span>
    <ul class="services">
      <li>Storm damage specialists</li>
      <li>Commercial &amp; residential shingles</li>
      <li>Flat and metal roofs.</li>
    </ul>
  </section>
</main>
</body>
</html>
```